Bakery Replacement Lighted Sign Face

We are opening a new bakery that sells only cakes. The name is "The Willow Lantern." We are replacing the current sign face with a new look that states our name and makes a bold statement of fun. We will be known for having 101 cakes that are always ready for immediate pickup or delivery. Our colors are pink, orange, and lime green. An image is provided to see the colors.

Target Market(s)

people who buy cakes for parties and all other occasions

Industry/Entity Type

Cakes

Other font styles liked:
• look at the logo and file for the main font name

Colors
59FF00
82FF00
B8FF75
E3FFCB
F4FFEA
F0912C
F2A743
F7CA91
FBE8D2
FDF5EE
EB3D1F
EC4F4E
F09395
F8D3D4
FCEDEE

Requirements
Must have
• The name of the bakery. Logo can be used as is or changed as shown in one of the uploaded PDFs. Must use either pink, orange, lime green, white, or black. We prefer a bright pink background with white lettering as our first choice, but are willing to be open minded to see all creative concepts. Also the sign is 14 feet long and 42 inches tall so the artwork must fit within those boundaries. Also keep in mind the sign does have a 4 inch black frame. So the graphics area is actually 13 feet 2 inches by 3 feet. Also, in the attached pdf that shows a rough possible layout, the words "101 cakes to go" is on the sign. It is NOT a must. Only use the wording if it adds to your design.
Nice to have
• You are welcome to add additional stars or other fun graphics that could look good.
Should not have
• No images of cakes or other bakery products.

```html
<!DOCTYPE html>
<html lang="en">
<head>
<meta charset="utf-8">
<title>The Willow Lantern – Sign Face</title>
<link href="https://fonts.googleapis.com/css2?family=Fredoka:wght@600&display=swap" rel="stylesheet">
<style>
  :root {
    --page: #ffffff;
    --pink: #ec3996;
    --orange: #f48c36;
    --lime: #afd44c;
    --white: #ffffff;
  }
  * { margin: 0; padding: 0; box-sizing: border-box; }
  html, body {
    width: 1200px;
    height: 900px;
    overflow: hidden;
    background: var(--page);
  }
  .canvas {
    position: relative;
    width: 1200px;
    height: 900px;
  }
  .sign-face {
    position: absolute;
    left: 50px;
    top: 312px;
    width: 1100px;
    height: 275px;
    overflow: hidden;
    font-family: "Fredoka", "Varela Round", sans-serif;
    font-weight: 600;
  }
  .sign-face__shapes {
    position: absolute;
    inset: 0;
    display: block;
  }
  .brand-name {
    position: absolute;
    left: 68px;
    top: 44px;
    width: 400px;
    color: var(--white);
    line-height: 0.95;
    letter-spacing: -0.5px;
  }
  .brand-name__line {
    display: block;
    font-size: 72px;
  }
  .brand-name__line--second {
    padding-left: 56px;
  }
  .tagline {
    position: absolute;
    left: 803px;
    top: 70px;
    width: 200px;
    text-align: center;
    color: var(--pink);
    line-height: 1;
  }
  .tagline__count {
    display: block;
    font-size: 62px;
    line-height: 52px;
    letter-spacing: 1px;
  }
  .tagline__words {
    display: block;
    font-size: 52px;
    line-height: 48px;
    letter-spacing: -0.5px;
  }
</style>
</head>
<body>
<main class="canvas">
  <section class="sign-face" aria-label="The Willow Lantern lighted sign face">
    <svg class="sign-face__shapes" width="1100" height="275" viewBox="0 0 1100 275" aria-hidden="true">
      <rect class="field" x="0" y="0" width="1100" height="275" fill="var(--pink)"/>
      <circle class="accent accent--orange" cx="170" cy="-35" r="250" fill="var(--orange)"/>
      <circle class="accent accent--lime" cx="905" cy="296" r="249" fill="var(--lime)"/>
      <rect class="safe-area" x="32.5" y="20" width="1035" height="236" fill="none" stroke="var(--white)" stroke-width="0.6"/>
    </svg>

    <h1 class="brand-name">
      <span class="brand-name__line">The Willow</span>
      <span class="brand-name__line brand-name__line--second">Lantern</span>
    </h1>

    <p class="tagline">
      <span class="tagline__count">101</span>
      <span class="tagline__words">cakes</span>
      <span class="tagline__words">to go</span>
    </p>
  </section>
</main>
</body>
</html>
```